Design Executive Business Acquisitons Brokerage Website

Modern but Professional with the colours black, purple and white. Must convey authenticity, and progressive out-of-square thinking. We are a boutique Business Broking firm located in Brisbane QLD Australia. We market and sell businesses with sales revenue/turnover from Au $1M to $15 M + or have a minimum staff of 15 to 50 staff. Our buyers are generally acquisitions corporate buyers. We need a modern approach but conservative tones. We are serious and experienced. We say it as it is and we get the job done! We sell in the following industries but not limited to, engineering, manufacturing, agriculture, recruitment, transportation, warehousing, services, IT,eCommerce, civil construction,mining, wholesaling, dealerships, MEdical (all), service stations, Management rights, high-end retail, building construction,importing,exporting to name a few.

Target Market(s)

SME Corporate Public & Private exsisting large businesses that are looking to buy through acquisitions

Industry/Entity Type

Coommercial executive Business Sale

Number of Pages Required

5+ page

Font styles to use
Sans Serif

Requirements
Must have
• Serious tones, searchar, NDA form, serious corporate executive feel. Include all corporaate colors,black less whit purples.Corporate Logo
Nice to have
• carosel moving right to left of industry pictures as per above and attached industries
Should not have
• No hand shaking, business people.

```html
<!DOCTYPE html>
<html lang="en">
<head>
<meta charset="utf-8">
<title>The Team – Meridian Acquisitions Group</title>
<link rel="stylesheet" href="https://fonts.googleapis.com/css2?family=Poppins:wght@400;500;600;700&display=swap">
<style>
  :root {
    --purple: #563d87;
    --purple-deep: #4a3278;
    --purple-soft: #8b77b5;
    --ink: #1e1e24;
    --heading: #2f2f36;
    --white: #ffffff;
    --mist: #f1f1f3;
  }
  * { margin: 0; padding: 0; box-sizing: border-box; }
  html, body { width: 1200px; height: 2191px; overflow: hidden; }
  body {
    font-family: "Poppins", sans-serif;
    color: var(--ink);
    background: var(--white);
    position: relative;
  }
  .abs { position: absolute; }

  /* header */
  .site-header { position: absolute; left: 0; top: 0; width: 1200px; height: 85px; background: var(--white); }
  .search { left: 80px; top: 37px; display: flex; align-items: center; gap: 10px; font-size: 13px; color: var(--ink); }
  .brand { display: flex; align-items: center; gap: 8px; color: var(--purple); font-weight: 600; }
  .header-brand { left: 470px; top: 24px; font-size: 26px; }
  .brand-dot { width: 34px; height: 34px; border-radius: 50%; background: var(--purple); }
  .brand-sub { display: block; font-size: 10px; letter-spacing: 1.4px; margin-top: -6px; }
  .menu-icon { left: 954px; top: 36px; }
  .contact-btn {
    left: 1009px; top: 24px; width: 132px; height: 38px; background: var(--purple); color: var(--white);
    font-size: 11.5px; font-weight: 600; display: flex; align-items: center; justify-content: center; border-radius: 2px;
  }

  /* hero */
  .hero-photo {
    position: absolute; left: 0; top: 85px; width: 1200px; height: 470px;
    background: linear-gradient(135deg, #4a4540 0%, #7d746a 30%, #5c554e 55%, #2d2a27 100%);
  }
  .hero-title { left: 92px; top: 262px; font-size: 47px; font-weight: 700; color: var(--white); }
  .hero-curve { left: 0; top: 440px; }

  /* team intro */
  .section-bg {
    position: absolute; left: 0; top: 540px; width: 1200px; height: 1300px;
    background: linear-gradient(180deg, #ffffff 0%, #f3f3f5 40%, #f7f7f8 60%, #ffffff 100%);
  }
  .section-title { width: 1200px; left: 0; text-align: center; font-weight: 600; color: var(--heading); }
  .our-team { top: 538px; font-size: 36px; left: -17px; }
  .our-team span { color: var(--purple); }
  .rule { height: 2px; background: var(--purple-soft); }
  .rule::after { content: ""; position: absolute; left: 50%; top: -1px; width: 26px; height: 4px; margin-left: -13px; background: var(--purple); }
  .intro {
    left: 140px; top: 617px; width: 916px; font-size: 14.5px; line-height: 28.3px; text-align: center;
  }
  .story { left: 96px; width: 488px; font-size: 14.5px; line-height: 28.3px; text-align: justify; text-align-last: center; }
  .story-one { top: 768px; }
  .story-two { top: 966px; }

  .feature-photo {
    position: absolute; left: 648px; top: 764px; width: 436px; height: 333px;
    background: radial-gradient(circle at 55% 45%, #c9a24a 0%, #9b7a2f 35%, #3b3226 70%, #23211f 100%);
  }
  .accent-bar-v { left: 638px; top: 978px; width: 10px; height: 128px; background: var(--purple); }
  .accent-bar-h { left: 638px; top: 1097px; width: 109px; height: 9px; background: var(--purple); }

  /* key factors */
  .factors-title { top: 1214px; font-size: 24px; line-height: 35px; text-transform: uppercase; left: 12px; }
  .factors-lead { left: 190px; top: 1318px; width: 840px; text-align: center; font-size: 16px; line-height: 28.5px; }
  .factor { width: 400px; }
  .factor h3 { font-size: 14.5px; font-weight: 600; line-height: 19px; }
  .factor p { font-size: 13.5px; line-height: 17px; }
  .factor-mark { width: 16px; height: 16px; border-radius: 50%; background: var(--purple); }
  .closing { left: 110px; top: 1746px; width: 1000px; text-align: center; font-size: 14.5px; line-height: 29px; }

  /* footer */
  .footer-band { left: 0; top: 1820px; }
  .footer-brand { left: 68px; top: 1975px; font-size: 30px; color: var(--white); }
  .footer-brand .brand-dot { background: var(--white); width: 38px; height: 38px; }
  .social { left: 190px; top: 2040px; display: flex; gap: 8px; }
  .social span { width: 28px; height: 28px; border-radius: 50%; border: 2.5px solid var(--white); }
  .copyright { left: 70px; top: 2084px; width: 220px; text-align: right; color: var(--white); font-size: 13.5px; line-height: 17px; }
  .footer-col h4 { font-size: 19px; font-weight: 600; color: var(--white); margin-bottom: 6px; }
  .footer-col li { list-style: none; color: var(--white); font-size: 14px; line-height: 24.2px; padding-left: 3px; }
  .contact-line { display: flex; align-items: center; gap: 9px; color: var(--white); font-size: 13.5px; height: 30.5px; }
</style>
</head>
<body>

<header class="site-header">
  <div class="abs search">
    <svg width="16" height="16" viewBox="0 0 16 16"><circle cx="6.5" cy="6.5" r="5" fill="none" stroke="#563d87" stroke-width="2.2"/><line x1="10.2" y1="10.2" x2="14.5" y2="14.5" stroke="#563d87" stroke-width="2.4" stroke-linecap="round"/></svg>
    <span>TYPE HERE TO SEARCH</span>
  </div>
  <div class="abs brand header-brand">
    <span class="brand-dot"></span>
    <span>Meridian<span class="brand-sub">ACQUISITIONS GROUP</span></span>
  </div>
  <svg class="abs menu-icon" width="32" height="16" viewBox="0 0 32 16">
    <g stroke="#563d87" stroke-width="1.6"><line x1="0" y1="2" x2="32" y2="2"/><line x1="0" y1="8" x2="32" y2="8"/><line x1="0" y1="14" x2="32" y2="14"/></g>
  </svg>
  <div class="abs contact-btn">CONTACT US</div>
</header>

<div class="hero-photo" role="img" aria-label="Desk with laptop, notebook and drinks while a hand writes notes"></div>
<div class="section-bg"></div>
<svg class="abs hero-curve" width="1200" height="120" viewBox="0 0 1200 120">
  <path d="M0 110 Q600 -40 1200 110 L1200 120 L0 120 Z" fill="#ffffff"/>
  <path d="M12 106 Q600 -50 1188 104" fill="none" stroke="#563d87" stroke-width="6"/>
  <path d="M0 118 Q600 -28 1200 118" fill="none" stroke="#ffffff" stroke-width="10"/>
</svg>
<h1 class="abs hero-title">The Team</h1>

<h2 class="abs section-title our-team"><span>Our</span> Team</h2>
<div class="abs rule" style="left:515px;top:593px;width:139px;"></div>

<p class="abs intro">Once engaged, our highly skilled team will dedicate itself unreservedly to researching, analyzing and preparing your business for sale. We'll use our findings to develop a market value estimate, before confidentially marketing your company to a strategically targeted list of companies, private-equity groups and financial buyers.</p>

<p class="abs story story-one">In addition, the team at Meridian Acquisitions Group knows the vital role a well-written Information Memorandum (IM) can play in securing the interest of serious buyers. After working to gain a thorough understanding of your strengths and value drivers, we'll present them to prospective buyers via a comprehensive, informative and easy-to-understand Information Memorandum.</p>
<p class="abs story story-two">At Meridian Acquisitions Group, our primary objective is to gather a wide range of inquiries that lead to attractive offers for your consideration. Through expert consultation with you and your trusted advisors, we will harness our unrivalled negotiation skills to effectively secure the deal with the buyer, ensuring a successful transaction.</p>

<div class="abs accent-bar-v"></div>
<div class="abs accent-bar-h"></div>
<div class="feature-photo" role="img" aria-label="Golden interlocking gears on a dark background"></div>

<h2 class="abs section-title factors-title">Key factors that make us the ideal collaborator for<br>successfully selling your business:</h2>
<div class="abs rule" style="left:548px;top:1300px;width:139px;"></div>
<p class="abs factors-lead">To summarize, throughout the process you will benefit from access to the following intelligence, meaning you'll be best positioned to make the smartest decision...</p>

<span class="abs factor-mark" style="left:160px;top:1418px"></span>
<div class="abs factor" style="left:190px;top:1414px">
  <h3>Vast Expertise</h3>
  <p>We possess extensive experience in assisting SMEs with successful business acquisitions.</p>
</div>
<span class="abs factor-mark" style="left:615px;top:1418px"></span>
<div class="abs factor" style="left:646px;top:1414px">
  <h3>Tailored Approach:</h3>
  <p>We develop customized strategies to effectively market and showcase your business's unique value.</p>
</div>
<span class="abs factor-mark" style="left:160px;top:1521px"></span>
<div class="abs factor" style="left:190px;top:1517px;width:360px">
  <h3>Comprehensive Market Knowledge</h3>
  <p>We have in-depth understanding of the market trends, ensuring accurate valuation and strategic positioning.</p>
</div>
<span class="abs factor-mark" style="left:615px;top:1516px"></span>
<div class="abs factor" style="left:646px;top:1517px">
  <h3>Confidentiality Assurance</h3>
  <p>We prioritize confidentiality throughout the listing process to protect your business's sensitive information.</p>
</div>
<span class="abs factor-mark" style="left:160px;top:1640px"></span>
<div class="abs factor" style="left:190px;top:1636px">
  <h3>Extensive Network</h3>
  <p>Our wide network of buyers and investors enables us to connect you with the right prospects.</p>
</div>
<span class="abs factor-mark" style="left:615px;top:1640px"></span>
<div class="abs factor" style="left:646px;top:1636px;width:430px">
  <h3>Negotiation Prowess</h3>
  <p>Our skilled negotiators strive to secure the best possible deal for you, maximizing your business's value.</p>
</div>

<p class="abs closing">At Meridian Acquisitions Group, our dedication lies in prioritizing with a client-first approach. We provide transparent and honest advice, coupled with comprehensive education, to guarantee high levels of comfort at every stage without any exceptions.</p>

<svg class="abs footer-band" width="1200" height="371" viewBox="0 0 1200 371">
  <path d="M0 13 Q600 170 1200 13 L1200 371 L0 371 Z" fill="#563d87"/>
  <path d="M110 40 Q600 170 1090 40 Q600 150 110 40 Z" fill="#ffffff"/>
  <path d="M120 42 Q600 140 1085 42" fill="none" stroke="#4a3278" stroke-width="3"/>
</svg>

<div class="abs brand footer-brand">
  <span class="brand-dot"></span>
  <span>Meridian<span class="brand-sub" style="font-size:11px">ACQUISITIONS GROUP</span></span>
</div>
<div class="abs social"><span></span><span></span><span></span></div>
<p class="abs copyright">© 2023 Meridian Acquisitions<br>All Rights Reserved</p>

<div class="abs footer-col" style="left:377px;top:1974px">
  <h4>Our Services</h4>
  <ul><li>Sell a business</li><li>Buy a business</li><li>Appraise a business</li></ul>
</div>
<div class="abs footer-col" style="left:585px;top:1969px">
  <h4>Usefull links</h4>
  <ul><li>Home</li><li>About Us</li><li>Business For Sale</li><li>FAQ's</li><li>Blogs</li><li>Contact Us</li></ul>
</div>
<div class="abs footer-col" style="left:782px;top:1972px">
  <h4>Contact Us</h4>
  <div class="contact-line">
    <svg width="16" height="16" viewBox="0 0 24 24"><path d="M6.6 10.8a15 15 0 0 0 6.6 6.6l2.2-2.2c.3-.3.7-.4 1-.2 1.1.4 2.3.6 3.6.6.6 0 1 .4 1 1V20c0 .6-.4 1-1 1C10.6 21 3 13.4 3 4c0-.6.4-1 1-1h3.5c.6 0 1 .4 1 1 0 1.3.2 2.5.6 3.6.1.3 0 .7-.2 1z" fill="#ffffff"/></svg>
    <span>+61400112233</span>
  </div>
  <div class="contact-line">
    <svg width="16" height="12" viewBox="0 0 16 12"><rect x="0" y="0" width="16" height="12" fill="#ffffff"/><path d="M0 0 L8 7 L16 0" fill="none" stroke="#563d87" stroke-width="1.4"/></svg>
    <span>inquiry@meridianacquisitions.com.au</span>
  </div>
  <div class="contact-line" style="padding-left:25px">harper.lane@meridianacquisitions.com.au</div>
</div>

</body>
</html>
```